Veltro Coaching Business Card

We need a business card designed for a a company called "Veltro Coaching". We offer consulting, coaching and training to business leaders and coaches (across the world) using the latest findings in neuroscience, social and emotional intelligence and positive psychology. The final design should communicate the use of brain science to create sustainable relationships.

The card should be doublesided. The logo is attached and names and titles will be provided to the successful designer. Thank you.

Industry/Entity Type

Training

```html
<!DOCTYPE html>
<html lang="en">
<head>
<meta charset="utf-8">
<title>Veltro Coaching – Business Card</title>
<link rel="stylesheet" href="https://fonts.googleapis.com/css2?family=Lato:ital,wght@0,300;0,400;0,700;1,400&family=Noto+Serif:ital,wght@1,700&display=swap">
<style>
  :root {
    --brand-blue: #0a8dc4;
    --brand-green: #b6d31c;
    --ink: #2b2b2b;
    --paper: #ffffff;
    --backdrop: #e4e8eb;
  }
  * { box-sizing: border-box; margin: 0; padding: 0; }
  html, body { width: 1200px; height: 960px; overflow: hidden; }
  body {
    background: var(--backdrop);
    font-family: "Lato", sans-serif;
    position: relative;
  }
  .card {
    position: absolute;
    left: 250px;
    width: 700px;
    height: 400px;
    overflow: hidden;
    box-shadow: 0 6px 18px rgba(0,0,0,0.12);
  }

  /* Front side */
  .card--front { top: 60px; background: var(--paper); }
  .holder { position: absolute; left: 56px; top: 64px; }
  .holder__name {
    font-weight: 300;
    font-size: 34px;
    letter-spacing: 0.5px;
    color: var(--ink);
    text-transform: uppercase;
    padding-bottom: 6px;
    border-bottom: 2px solid var(--brand-blue);
    display: inline-block;
  }
  .holder__title {
    font-style: italic;
    font-size: 20px;
    color: var(--ink);
    margin-top: 8px;
  }
  .brand {
    position: absolute;
    right: 40px;
    top: 120px;
    width: 290px;
    text-align: center;
  }
  .brand__mark {
    display: flex;
    align-items: center;
    justify-content: center;
    gap: 10px;
  }
  .brand__dot {
    width: 16px; height: 16px;
    background: var(--brand-green);
    flex: none;
  }
  .brand__name {
    font-weight: 700;
    font-size: 32px;
    color: var(--brand-blue);
    white-space: nowrap;
  }
  .tagline {
    font-family: "Noto Serif", serif;
    font-style: italic;
    font-weight: 700;
    font-size: 17px;
    color: var(--brand-blue);
    margin-top: 40px;
    white-space: nowrap;
  }
  .contacts {
    position: absolute;
    left: 60px;
    bottom: 70px;
    list-style: none;
  }
  .contacts li {
    display: flex;
    align-items: center;
    gap: 14px;
    font-size: 19px;
    color: var(--ink);
    line-height: 30px;
  }
  .contacts svg { width: 18px; height: 18px; fill: var(--brand-blue); flex: none; }
  .contacts .web { font-weight: 700; }
  .contacts .web em { font-style: normal; color: var(--brand-blue); }
  .band { position: absolute; bottom: 0; }
  .band--blue { left: 0; width: 58%; height: 14px; background: var(--brand-blue); }
  .band--green { right: 0; width: 42%; height: 44px; background: var(--brand-green); }

  /* Back side */
  .card--back {
    top: 500px;
    background: var(--brand-blue);
    color: var(--paper);
    text-align: center;
  }
  .card--back .brand {
    position: static;
    width: auto;
    margin-top: 130px;
  }
  .card--back .brand__name { color: var(--paper); font-size: 44px; }
  .card--back .brand__dot { width: 20px; height: 20px; }
  .card--back .site { font-size: 16px; letter-spacing: 1.5px; margin-top: 8px; font-weight: 700; }
  .card--back .tagline { color: var(--paper); margin-top: 28px; font-size: 20px; letter-spacing: 1px; }
</style>
</head>
<body>
  <section class="card card--front" aria-label="Card front">
    <div class="holder">
      <h1 class="holder__name">Hannah Whitcombe</h1>
      <p class="holder__title">Director</p>
    </div>

    <div class="brand">
      <div class="brand__mark">
        <span class="brand__dot"></span>
        <span class="brand__name">Veltro Coaching</span>
      </div>
      <p class="tagline">brain-led growth for teams</p>
    </div>

    <ul class="contacts">
      <li>
        <svg viewBox="0 0 24 24" aria-hidden="true"><path d="M7 1h10a2 2 0 0 1 2 2v18a2 2 0 0 1-2 2H7a2 2 0 0 1-2-2V3a2 2 0 0 1 2-2zm0 3v11h10V4H7zm2 13v2h2v-2H9zm4 0v2h2v-2h-2z"/></svg>
        <span>+61 400 555 012</span>
      </li>
      <li>
        <svg viewBox="0 0 24 24" aria-hidden="true"><path d="M2 4h20v16H2V4zm2 2v.5l8 6 8-6V6H4zm0 3v9h16V9l-8 6-8-6z"/></svg>
        <span>hannah@veltrocoaching.com</span>
      </li>
      <li class="web">
        <svg viewBox="0 0 24 24" aria-hidden="true"><path d="M12 2 1 12h3v10h6v-6h4v6h6V12h3L12 2z"/></svg>
        <span>www.<em>veltrocoaching</em>.com</span>
      </li>
    </ul>

    <div class="band band--blue"></div>
    <div class="band band--green"></div>
  </section>

  <section class="card card--back" aria-label="Card back">
    <div class="brand">
      <div class="brand__mark">
        <span class="brand__dot"></span>
        <span class="brand__name">Veltro Coaching</span>
      </div>
      <p class="site">www.veltrocoaching.com</p>
      <p class="tagline">brain-led growth for teams</p>
    </div>
  </section>
</body>
</html>
```